WebDesign Flyer - A5 Double Sided

We create a complete web presence for local businesses.
A comprehensive background on our services and company can be found at www.keenpixelhouse.co.uk and on the attached sales document.

We want these flyers (a5, double sided, colour) to portray us as a local, professional and friendly service that will take care fully of a business's online presence. This includes website, hosting, email, domain AND IMPORTANTLY: we also can build them a business profile on business directory websites such as NookFinder, StreetBrowse, Marbel Spots, Zorb etc. which helps them increase their profit.

Target Market(s)

Small to medium businesses found on the high street. eg: restaurants, physios, doctors, retail shops, salons, hairdressers, as well as more corporate businesses like accountancy firms and lawyers.

Industry/Entity Type

Business Directory

Requirements
Must have
• Full project files provided with all required elements if design is chosen. Design to mention: sites can be updated in less than 1 minute in 3 clicks, No contracts, money back guarantee (no risk), prices from £400, SEO as standard, keenpixelhouse.co.uk, 020 7946 0318, info@keenpixelhouse.co.uk, 10% discount with this flyer until December 20th 2010.
Nice to have
• To mention: dedicated support, business photos (see keenpixelhouse.co.uk/features), Chatterly, Quippo, ReelBox, Snapry, WorkNest Integration, free consultation, logos of services we provide (see logos.zip for examples).
Should not have
• our logo featured too prominently.

```html
<!DOCTYPE html>
<html lang="en">
<head>
<meta charset="utf-8">
<title>Keen Pixel House – A5 Flyer</title>
<link href="https://fonts.googleapis.com/css2?family=Anton&family=Archivo+Black&family=Didact+Gothic&family=Nunito:wght@700;800;900&display=swap" rel="stylesheet">
<style>
  :root {
    --stage: #a7a9ac;
    --brand-blue: #1b93d8;
    --deep-blue: #1768b3;
    --chevron-blue: #7cc0ee;
    --sun-yellow: #f3ee3c;
    --paper: #ffffff;
  }
  * { margin: 0; padding: 0; box-sizing: border-box; }
  html, body { width: 1200px; height: 900px; overflow: hidden; }
  body { background: var(--stage); position: relative; font-family: "Didact Gothic", sans-serif; }

  .flyer { position: absolute; top: 250px; width: 540px; height: 390px; overflow: hidden; background: var(--brand-blue); white-space: nowrap; }
  .flyer--front { left: 40px; }
  .flyer--back { left: 620px; }

  /* FRONT */
  .headline { position: absolute; left: 0; line-height: 1; }
  .headline--increase { top: 8px; left: 12px; font-family: "Archivo Black", sans-serif; font-size: 64px; letter-spacing: 3px; color: var(--sun-yellow); }
  .headline--your-profit { top: 74px; left: 12px; font-family: "Anton", sans-serif; font-size: 74px; }
  .outline-word { color: transparent; -webkit-text-stroke: 3px var(--sun-yellow); letter-spacing: 1px; }
  .solid-white { color: var(--paper); }
  .headline--effective { top: 152px; left: 12px; font-family: "Anton", sans-serif; font-size: 74px; color: var(--sun-yellow); display: flex; align-items: center; }
  .with-an { font-family: "Archivo Black", sans-serif; font-size: 11px; writing-mode: vertical-rl; transform: rotate(180deg); margin-right: 4px; color: var(--sun-yellow); }
  .headline--website { top: 234px; left: 10px; font-family: "Archivo Black", sans-serif; font-size: 62px; color: var(--paper); letter-spacing: -1px; }
  .chevrons { position: absolute; right: 8px; top: 140px; }

  .offer-band { position: absolute; left: 0; bottom: 0; width: 100%; height: 76px; background: var(--paper); display: flex; align-items: center; padding-left: 14px; }
  .brand { display: flex; align-items: center; gap: 6px; }
  .brand__mascot { width: 34px; height: 58px; border-radius: 4px; background: linear-gradient(180deg, var(--sun-yellow), var(--chevron-blue)); }
  .brand__name { font-family: "Nunito", sans-serif; font-weight: 900; font-size: 18px; line-height: 1; color: var(--deep-blue); white-space: normal; width: 90px; }
  .offer { margin-left: 28px; color: var(--brand-blue); font-family: "Archivo Black", sans-serif; line-height: 0.95; }
  .offer__big { font-size: 38px; letter-spacing: -1px; }
  .offer__small { font-size: 17px; }

  /* BACK */
  .intro-band { position: absolute; top: 0; left: 0; width: 100%; height: 86px; background: var(--paper); }
  .intro { position: absolute; left: 18px; top: 10px; width: 370px; white-space: normal; color: var(--brand-blue); font-family: "Nunito", sans-serif; font-weight: 800; font-size: 13px; line-height: 1.2; }
  .intro-band .brand { position: absolute; right: 14px; top: 14px; }
  .intro-band .brand__mascot { width: 28px; height: 50px; }
  .intro-band .brand__name { font-size: 16px; width: 80px; }

  .benefits { position: absolute; left: 18px; top: 92px; color: var(--paper); font-size: 13px; line-height: 1.25; }
  .benefits__list { color: var(--sun-yellow); }
  .why-title { position: absolute; left: 18px; top: 146px; color: var(--paper); font-size: 13px; }
  .reasons { position: absolute; left: 30px; top: 163px; color: var(--paper); font-size: 9.5px; line-height: 1.22; list-style: disc; }

  .starburst { position: absolute; right: 10px; top: 148px; width: 132px; height: 132px; }
  .starburst__text { position: absolute; inset: 0; display: flex; flex-direction: column; align-items: center; justify-content: center; transform: rotate(-18deg); color: var(--brand-blue); font-family: "Archivo Black", sans-serif; line-height: 0.9; text-align: center; }
  .starburst__pct { font-size: 34px; }
  .starburst__word { font-size: 15px; }
  .starburst__sub { font-size: 9px; }
  .starburst__terms { font-family: "Didact Gothic", sans-serif; font-size: 5px; margin-top: 2px; }

  .partner-strip { position: absolute; left: 14px; top: 290px; width: 512px; height: 24px; background: var(--paper); display: flex; align-items: center; justify-content: space-around; }
  .partner { font-family: "Nunito", sans-serif; font-weight: 800; font-size: 10px; color: var(--deep-blue); display: flex; align-items: center; gap: 3px; }
  .partner__dot { width: 7px; height: 7px; background: var(--brand-blue); }

  .contact-line { position: absolute; left: 30px; top: 320px; color: var(--sun-yellow); font-size: 15px; }
  .url-band { position: absolute; left: 0; bottom: 0; width: 100%; height: 46px; background: var(--paper); display: flex; align-items: center; justify-content: center; }
  .url { font-family: "Nunito", sans-serif; font-weight: 900; font-size: 35px; color: var(--brand-blue); letter-spacing: -0.5px; }
</style>
</head>
<body>

<section class="flyer flyer--front" aria-label="Flyer front">
  <div class="headline headline--increase">INCREASE</div>
  <div class="headline headline--your-profit"><span class="outline-word">YOUR</span><span class="solid-white">PROFIT</span></div>
  <div class="headline headline--effective"><span class="with-an">WITH AN</span>EFFECTIVE</div>
  <div class="headline headline--website">WEBSITE...</div>
  <svg class="chevrons" width="36" height="130" viewBox="0 0 36 130" aria-hidden="true">
    <polyline points="6,6 30,30 6,54" fill="none" stroke="var(--chevron-blue)" stroke-width="9"/>
    <polyline points="6,72 30,96 6,120" fill="none" stroke="var(--chevron-blue)" stroke-width="9"/>
  </svg>
  <div class="offer-band">
    <div class="brand">
      <div class="brand__mascot" role="img" aria-label="Superhero mascot illustration"></div>
      <div class="brand__name">Keen Pixel House</div>
    </div>
    <div class="offer">
      <div class="offer__big">10% DISCOUNT</div>
      <div class="offer__small">WITH THIS FLYER</div>
    </div>
  </div>
</section>

<section class="flyer flyer--back" aria-label="Flyer back">
  <div class="intro-band">
    <p class="intro">We focus on small businesses who want to start increasing profit through an effective online presence. Our packages are tailored, our service is reliable and our prices are competitive.</p>
    <div class="brand">
      <div class="brand__mascot" role="img" aria-label="Superhero mascot illustration"></div>
      <div class="brand__name">Keen Pixel House</div>
    </div>
  </div>

  <div class="benefits">
    <div>Benefits of having an online presence include:</div>
    <div class="benefits__list">Increase Sales // Save Money on Advertising // Increase Enquiries //</div>
    <div class="benefits__list">Your Business is Always Open // Improve Credibility // Free Market Research</div>
  </div>
  <div class="why-title">Why chose us?</div>
  <ul class="reasons">
    <li>We provide an all-in-one tailored package for your business.</li>
    <li>Sites can be updated in less than 1 minute in 3 clicks</li>
    <li>We never make you sign a contract.</li>
    <li>Money back guarantee (no risk)</li>
    <li>Prices from £400 - amongst the lowest on the Internet</li>
    <li>Search Engine Optimisation as standard</li>
    <li>While your site is hosted by us, we provide FREE technical support</li>
    <li>Absolutely zero hidden fees</li>
    <li>Free consultation</li>
    <li>Some of the services we can integrate you website with include:</li>
  </ul>

  <div class="starburst">
    <svg width="132" height="132" viewBox="0 0 132 132" aria-hidden="true">
      <polygon fill="var(--sun-yellow)" points="130,66 118.2,80 121.4,98 104.2,104.2 98,121.4 80,118.2 66,130 52,118.2 34,121.4 27.8,104.2 10.6,98 13.8,80 2,66 13.8,52 10.6,34 27.8,27.8 34,10.6 52,13.8 66,2 80,13.8 98,10.6 104.2,27.8 121.4,34 118.2,52"/>
    </svg>
    <div class="starburst__text">
      <div class="starburst__pct">10%</div>
      <div class="starburst__word">DISCOUNT*</div>
      <div class="starburst__sub">WITH THIS FLYER</div>
      <div class="starburst__terms">*Offer valid until December 20th 2010</div>
    </div>
  </div>

  <div class="partner-strip">
    <span class="partner"><span class="partner__dot"></span>Chatterly</span>
    <span class="partner">Quippo</span>
    <span class="partner">WorkNest</span>
    <span class="partner">ReelBox</span>
    <span class="partner">Zorb</span>
    <span class="partner">TradeLeaf</span>
    <span class="partner">NookFinder</span>
    <span class="partner">Marbel Spots</span>
  </div>

  <div class="contact-line">Call: 020 7946 0318 Email: info@keenpixelhouse.co.uk</div>
  <div class="url-band"><span class="url">keenpixelhouse.co.uk</span></div>
</section>

</body>
</html>
```